Bright, Fun and hard to forget home inspection business card.

We need a Business card design for a new Home Inspection company. We are building a brand that is bright, fun and easy to remember.

Target Market(s)

Anyone involed in buying and selling of homes.

Industry/Entity Type

Home Inspection

Contact Information for Business Card

Colin Marlowe Owner/Inspector

Wedsite- PorchAndRafterCheck.example
Phone: 253-555-0187
Email- ColinMarlowe@mailbox.example
WA Lic # 4806

Requirements
Must have
• BRQV LOGO somewhere on card.

```html
<!DOCTYPE html>
<html lang="en">
<head>
<meta charset="utf-8">
<title>Porch &amp; Rafter Check – Business Card</title>
<link rel="stylesheet" href="https://fonts.googleapis.com/css2?family=Exo+2:wght@400;600;800&display=swap">
<style>
  :root {
    --brand-orange: #f26135;
    --ink: #2b2b2b;
    --swoosh: #333333;
    --paper: #ffffff;
    --backdrop: #dcdcdc;
    --card-w: 540px;
    --card-h: 309px;
  }
  * { margin: 0; padding: 0; box-sizing: border-box; }
  html, body {
    width: 1200px;
    height: 771px;
    overflow: hidden;
  }
  body {
    background: var(--backdrop);
    font-family: "Exo 2", sans-serif;
    color: var(--ink);
    position: relative;
  }
  .card {
    position: absolute;
    top: 231px;
    width: var(--card-w);
    height: var(--card-h);
    background: var(--paper);
    overflow: hidden;
    box-shadow: 0 2px 6px rgba(0,0,0,0.12);
  }
  .card--front { left: 45px; }
  .card--back  { left: 615px; }

  .card__art {
    position: absolute;
    inset: 0;
    width: 100%;
    height: 100%;
  }
  .contact-name {
    position: absolute;
    top: 26px;
    right: 250px;
    text-align: right;
    font-weight: 600;
    font-size: 17px;
    letter-spacing: 1.5px;
    text-transform: uppercase;
  }
  .contact-role {
    display: block;
    font-weight: 400;
    font-size: 11px;
    letter-spacing: 0.5px;
    text-transform: none;
    margin-top: 2px;
  }
  .contact-address {
    position: absolute;
    top: 92px;
    right: 250px;
    text-align: right;
    font-size: 11px;
    line-height: 1.4;
  }
  .contact-list {
    position: absolute;
    left: 26px;
    bottom: 34px;
    list-style: none;
    font-size: 11px;
    line-height: 1;
  }
  .contact-list li {
    display: flex;
    align-items: center;
    gap: 8px;
    margin-top: 8px;
  }
  .contact-list svg {
    width: 12px;
    height: 12px;
    flex: none;
    fill: var(--ink);
  }

  .brand-mark {
    position: absolute;
    display: flex;
    align-items: center;
    gap: 10px;
    font-weight: 800;
    color: var(--ink);
    text-transform: uppercase;
    line-height: 1;
  }
  .brand-mark__dot {
    flex: none;
    border-radius: 50%;
    background: var(--brand-orange);
  }
  .card--front .brand-mark {
    right: 22px;
    top: 128px;
    font-size: 17px;
    width: 170px;
  }
  .card--front .brand-mark__dot { width: 22px; height: 22px; }
  .card--back .brand-mark {
    left: 50%;
    top: 50%;
    transform: translate(-50%, -50%);
    font-size: 30px;
    width: 360px;
    gap: 14px;
  }
  .card--back .brand-mark__dot { width: 38px; height: 38px; }
</style>
</head>
<body>

  <section class="card card--front" aria-label="Business card front">
    <svg class="card__art" viewBox="0 0 540 309" aria-hidden="true">
      <path d="M0 0 H330 C296 90 296 220 352 309 H0 Z" fill="var(--brand-orange)"/>
      <path d="M330 0 C296 90 296 220 352 309 L358 309 C312 220 318 92 356 0 Z" fill="var(--swoosh)"/>
    </svg>

    <h1 class="contact-name">Colin Marlowe
      <span class="contact-role">Owner / Inspector</span>
    </h1>
    <p class="contact-address">WA Lic # 4806<br>Tacoma WA</p>

    <ul class="contact-list">
      <li>
        <svg viewBox="0 0 12 12"><path d="M2.5 0.5l2 2.5-1 1.2c.7 1.6 1.7 2.6 3.3 3.3l1.2-1 2.5 2-1 2C5.5 10.5 1.5 6.5 0.5 1.5z"/></svg>
        253-555-0187
      </li>
      <li>
        <svg viewBox="0 0 12 12"><path d="M3 0h6v12H3z M4 1.5v8h4v-8z"/></svg>
        253-555-0187
      </li>
      <li>
        <svg viewBox="0 0 12 12"><path d="M0 2h12v8H0z M1 3l5 3.5L11 3v-.2H1z"/></svg>
        ColinMarlowe@mailbox.example
      </li>
      <li>
        <svg viewBox="0 0 12 12"><path d="M6 0a6 6 0 1 0 .01 0z M6 1.2a4.8 4.8 0 1 1-.01 0z M1 5.5h10v1H1z M5.5 1h1v10h-1z"/></svg>
        PorchAndRafterCheck.example
      </li>
    </ul>

    <div class="brand-mark">
      <span class="brand-mark__dot"></span>
      <span class="brand-mark__name">Porch &amp; Rafter Check LLC</span>
    </div>
  </section>

  <section class="card card--back" aria-label="Business card back">
    <div class="brand-mark">
      <span class="brand-mark__dot"></span>
      <span class="brand-mark__name">Porch &amp; Rafter Check LLC</span>
    </div>
  </section>

</body>
</html>
```